Psychotherapy Website - Based in London

I am a newly trained psychotherapist and need a new website for www.rosalindfaber.co.uk.

I offer therapy for addiction, relationships, trauma and many other issues people face in their lives.

I want the website to be welcoming, gentle, feminine and for people to feel safe.

I do not like a page site that scrolls through sections, rather each page should be separate. Here some examples that i like. Sectional rather than scrolled.

https://www.hettiemarsh.com/
https://www.thequietwardrooms.com/

The imagery should be around pink using the flower in the logo / wording and around the site:

Here is a link to the flower for ideas:
https://www.pictofind.net/search?q=pink+gerbera&rlz=2D4KQTW_en-GBGB415GB415&source=lnms&tbm=isch&sa=X&ved=7cvQRtrk482h3PxZTuKLmeNBwXW_1AtXpVlKDbOQBmFLB&biw=1500&bih=889&dpr=2

RosalindFaber
Compassionate Psychotherapy

Is the logo and subheader for the website. Please use a typeface for the name that is appealing and professional.

Type face similar NOT EXLUSIVLY - JUST AN IDEA like this:
https://glowtonicstudio.com/

Basic business card i created as a rough idea below.

I have also added the website copy.

The headers are

Homepage
About Me
Therapy
Common Questions
Blog
Contact Me

Target Market(s)

Clients who are dealing with stress, trauma, pain, addiction

Industry/Entity Type

Therapy and Psychology

Coding

Coded - Design and coding required

Number of Pages Required

5+ page

Font styles to use
Serif
Sans Serif
Script

Colors
0054AA
0677BA
7BADD7
CADEEF
E8F1F8
0094D4
00A9DD
6FCCEA
C7EBF8
E9F6FB
E54698
E96AAD
F1A4CE
F9D9EA
FCEFF6

Requirements
Must have
• Pink Gerbera Flower integrated into design
Nice to have
• Images but not to stock imagery. Needs to look authentic and natural
Should not have
• Stock images of people. Images are important but needs to feel REAL

```html
<!DOCTYPE html>
<html lang="en">
<head>
<meta charset="utf-8">
<title>Rosalind Faber – Compassionate Psychotherapy</title>
<link rel="stylesheet" href="https://fonts.googleapis.com/css2?family=Montserrat:wght@300;400;500;600;700&family=Playfair+Display:wght@700&display=swap">
<style>
:root{
  --pink:#e96aad;
  --pink-soft:#f1a4ce;
  --pink-pale:#f9d9ea;
  --ink:#2e2e2e;
  --muted:#6e6e6e;
  --nav:#3a3a3a;
  --sidebar:#dcdde1;
  --divider:#4a4a4a;
  --rule:#cfcfcf;
  --white:#ffffff;
}
*{box-sizing:border-box;margin:0;padding:0}
html,body{width:1200px;height:5017px;overflow:hidden;background:var(--divider)}
body{font-family:"Montserrat",sans-serif;color:var(--ink)}
.page{position:relative;width:1200px;background:var(--white);overflow:hidden}
.page + .page{margin-top:51px}
.site-header{position:absolute;left:0;top:0;width:1200px;height:72px;border-bottom:1px solid var(--rule);background:var(--white);z-index:2}
.brand{position:absolute;left:24px;top:20px;display:flex;align-items:center;gap:10px}
.brand-mark{width:28px;height:28px;border-radius:50%;background:var(--pink-soft)}
.brand-name{font-family:"Playfair Display",serif;font-weight:700;font-size:24px;color:var(--pink)}
.contact-bar{position:absolute;right:45px;top:27px;display:flex;gap:34px;font-size:12.5px;color:var(--ink)}
.contact-bar span{display:flex;align-items:center;gap:6px}
.sidebar{position:absolute;left:0;top:72px;bottom:0;width:271px;background:var(--sidebar)}
.nav{list-style:none;position:absolute;left:50px;top:48px}
.nav li{font-size:19px;font-weight:400;color:var(--nav);height:43px;position:relative}
.nav li.active::before{content:"";position:absolute;left:-19px;top:9px;width:11px;height:11px;border-radius:50%;background:var(--pink-soft)}
.social{position:absolute;left:50px;bottom:48px;display:flex;gap:12px}
.social span{width:8px;height:8px;border-radius:50%;background:var(--ink)}
.main{position:absolute;left:318px;right:40px}
.main p{font-size:15px;line-height:1.3;margin-bottom:10px}
.intro{top:218px}
.about-text{top:208px;width:450px}
.portrait{position:absolute;left:795px;top:185px;width:405px;bottom:0;background:linear-gradient(180deg,#f4f1ef 0%,#efe0d2 40%,#e66b9b 75%,#e2558f 100%)}
.therapy-text{top:121px}
.therapy-text p{font-size:14.6px;margin-bottom:10px}
.help-title{font-size:20px;font-weight:500;margin:24px 0 14px}
.help-grid{display:grid;grid-template-columns:331px 294px 220px;row-gap:8px;list-style:none}
.help-grid li{font-size:13.5px;position:relative;padding-left:16px}
.help-grid li::before{content:"";position:absolute;left:0;top:5px;width:8px;height:8px;border-radius:50%;background:var(--pink-soft)}
.faq{top:216px}
.faq h3{font-size:15.5px;font-weight:700;margin-bottom:16px}
.faq p{color:var(--muted);font-weight:300;font-size:14.5px;margin-bottom:20px}
.faq .answer-gap{margin-bottom:42px}
.blog{top:119px}
.blog h3{font-size:13.5px;font-weight:700;margin-bottom:14px}
.blog p{font-size:13px;line-height:1.28;color:var(--muted);font-weight:300;margin-bottom:14px}
.blog h3.later{margin-top:24px}
.contact-form{position:absolute;left:318px;top:230px;width:440px}
.field{width:440px;height:33px;border:2px solid var(--ink);margin-bottom:12px;font-size:12px;color:#b5b5b5;padding:7px 12px;font-weight:300}
.field.message{height:172px}
.send{display:inline-block;margin-top:12px;background:#3a3a3a;color:var(--white);font-weight:700;font-size:17px;padding:6px 12px}
.contact-info{position:absolute;left:843px;top:220px;font-size:15.5px;line-height:1.32;font-weight:500;font-style:normal}
.contact-info .gap{margin-top:26px}
</style>
</head>
<body>

<!-- Homepage -->
<section class="page" style="height:750px">
  <header class="site-header">
    <div class="brand"><span class="brand-mark"></span><span class="brand-name">Rosalind Faber</span></div>
    <div class="contact-bar">
      <span><svg width="12" height="9" viewBox="0 0 12 9"><rect x="0.5" y="0.5" width="11" height="8" fill="none" stroke="#2e2e2e"/><path d="M0.5 0.5 6 5 11.5 0.5" fill="none" stroke="#2e2e2e"/></svg>rosalindfaber@gentlerooms.co.uk</span>
      <span><svg width="10" height="10" viewBox="0 0 10 10"><path d="M2 0.5 4 3 3 4.3a6 6 0 0 0 2.7 2.7L7 6l2.5 2-1.2 1.5C4.5 9.5 0.5 5.5 0.5 1.7Z" fill="#2e2e2e"/></svg>07700 900418</span>
    </div>
  </header>
  <aside class="sidebar">
    <ul class="nav"><li class="active">homepage</li><li>about me</li><li>therapy</li><li>common questions</li><li>blog</li><li>contact me</li></ul>
    <div class="social"><span></span><span></span><span></span></div>
  </aside>
  <div class="main intro">
    <p>Taking the first steps towards engaging in therapy can be a very personal journey.</p>
    <p>Whilst, it can be challenging, I will ensure to make this journey as safe and as comfortable for you as possible.</p>
    <p>Psychotherapy can help you see your current situation in new light, depth and clarity. It can change old and unhelpful perspectives and feelings about yourself and your life, and ultimately help you make positive changes. It might be the most important journey you'll ever make.</p>
    <p>I provide a and non-judgmental space where any issues can be explored in complete confidentiality.</p>
    <p>My practice is based in Westbury, where the room is homely, comfortable and welcoming. I believe a good environment contributes to great therapy.</p>
    <p>Alternately, I am also available to provide therapy online, if this environment is more accommodating for my clients.</p>
    <p>I am passionate about improving mental health and committed to offering therapy to all individuals regardless of their age, race, culture, disability, sexual orientation, or socio-economic background.</p>
  </div>
</section>

<!-- About me -->
<section class="page" style="height:750px">
  <header class="site-header">
    <div class="brand"><span class="brand-mark"></span><span class="brand-name">Rosalind Faber</span></div>
    <div class="contact-bar">
      <span><svg width="12" height="9" viewBox="0 0 12 9"><rect x="0.5" y="0.5" width="11" height="8" fill="none" stroke="#2e2e2e"/><path d="M0.5 0.5 6 5 11.5 0.5" fill="none" stroke="#2e2e2e"/></svg>rosalindfaber@gentlerooms.co.uk</span>
      <span><svg width="10" height="10" viewBox="0 0 10 10"><path d="M2 0.5 4 3 3 4.3a6 6 0 0 0 2.7 2.7L7 6l2.5 2-1.2 1.5C4.5 9.5 0.5 5.5 0.5 1.7Z" fill="#2e2e2e"/></svg>07700 900418</span>
    </div>
  </header>
  <aside class="sidebar">
    <ul class="nav"><li>homepage</li><li class="active">about me</li><li>therapy</li><li>common questions</li><li>blog</li><li>contact me</li></ul>
    <div class="social"><span></span><span></span><span></span></div>
  </aside>
  <div class="main about-text">
    <p>I have over 10 years' experience of dealing with addictions. Addictions are often more of a solution to fear and emotional pain. However, eventually the addiction causes more problems. I know recovery is possible with the right support.</p>
    <p>I have also had some twenty years of experience of dealing with mental health issues such as depression, anxiety, complex PTSD and trauma. It is possible to manage these issues and live a full life.</p>
    <p>I have worked in the voluntary sector as a Listening Line volunteer and I am currently a therapist for Haven.</p>
  </div>
  <div class="portrait" role="img" aria-label="Portrait photograph of the therapist in a pink top against a white background"></div>
</section>

<!-- Therapy -->
<section class="page" style="height:808px">
  <header class="site-header">
    <div class="brand"><span class="brand-mark"></span><span class="brand-name">Rosalind Faber</span></div>
    <div class="contact-bar">
      <span><svg width="12" height="9" viewBox="0 0 12 9"><rect x="0.5" y="0.5" width="11" height="8" fill="none" stroke="#2e2e2e"/><path d="M0.5 0.5 6 5 11.5 0.5" fill="none" stroke="#2e2e2e"/></svg>rosalindfaber@gentlerooms.co.uk</span>
      <span><svg width="10" height="10" viewBox="0 0 10 10"><path d="M2 0.5 4 3 3 4.3a6 6 0 0 0 2.7 2.7L7 6l2.5 2-1.2 1.5C4.5 9.5 0.5 5.5 0.5 1.7Z" fill="#2e2e2e"/></svg>07700 900418</span>
    </div>
  </header>
  <aside class="sidebar">
    <ul class="nav"><li>homepage</li><li>about me</li><li class="active">therapy</li><li>common questions</li><li>blog</li><li>contact me</li></ul>
    <div class="social"><span></span><span></span><span></span></div>
  </aside>
  <div class="main therapy-text">
    <p>There are times when the challenges of life can make us feel overwhelmed and isolated, and it may feel difficult to talk about how we feel to those who are closest to us. We go through transitions and crises and experience uncertainty and loss. How we deal with difficulties in life is an important aspect in how we carry on forwards and ultimately who we become as people.</p>
    <p>I offer a range of psychotherapeutic approaches including transactional analysis psychotherapy and relational therapy.</p>
    <p>Through the process of exploration, we enable self-knowledge and self-awareness to help you grow and conquer issues that may previously have been experienced as all-consuming or overwhelming. We will not only look at your problems in the present but also identify the roots of these problems from your past. We will explore how your past experiences may have affected the way you live today and operate within your life in the present and when you become aware and understand this, it is possible for change to take place.</p>
    <p>Therapy can help you to develop ways of coping better and overcoming issues you may feel are holding you back. I can help you find and develop your personal strengths and help identify what is meaningful to you in life. By doing this, you will be able to move towards the kind of life you would like to live.</p>
    <h2 class="help-title">What we can help with</h2>
    <ul class="help-grid">
      <li>Addiction</li><li>Anger</li><li>Anxiety</li>
      <li>Bullying</li><li>Career Changes</li><li>Crisis/Breakdowns</li>
      <li>Depression</li><li>Difficulty making decisions</li><li>Emotional abuse</li>
      <li>Fear</li><li>Feeling alone/isolated</li><li>Health issues</li>
      <li>HIV</li><li>Identity issues</li><li>Low self confidence</li>
      <li>Less of meaning</li><li>LGBT issues</li><li>Negative thinking</li>
      <li>Porblems with Motivation/Focus</li><li>Psychosis</li><li>Relationship problems</li>
      <li>Self sabotage</li><li>Sexual abuse</li><li>Sexuality</li>
      <li>Stress</li><li>Substance misuse</li>
    </ul>
  </div>
</section>

<!-- Common questions -->
<section class="page" style="height:750px">
  <header class="site-header">
    <div class="brand"><span class="brand-mark"></span><span class="brand-name">Rosalind Faber</span></div>
    <div class="contact-bar">
      <span><svg width="12" height="9" viewBox="0 0 12 9"><rect x="0.5" y="0.5" width="11" height="8" fill="none" stroke="#2e2e2e"/><path d="M0.5 0.5 6 5 11.5 0.5" fill="none" stroke="#2e2e2e"/></svg>rosalindfaber@gentlerooms.co.uk</span>
      <span><svg width="10" height="10" viewBox="0 0 10 10"><path d="M2 0.5 4 3 3 4.3a6 6 0 0 0 2.7 2.7L7 6l2.5 2-1.2 1.5C4.5 9.5 0.5 5.5 0.5 1.7Z" fill="#2e2e2e"/></svg>07700 900418</span>
    </div>
  </header>
  <aside class="sidebar">
    <ul class="nav"><li>homepage</li><li>about me</li><li>therapy</li><li class="active">common questions</li><li>blog</li><li>contact me</li></ul>
    <div class="social"><span></span><span></span><span></span></div>
  </aside>
  <div class="main faq">
    <h3>How long will I need therapy for?</h3>
    <p>Therapy can last anywhere from one session to several months or even years. It all depends on what you want and need. Some people come to therapy with a very specific problem they need to solve and might find that one or two sessions is sufficient.</p>
    <p class="answer-gap">Other people come to therapy with more complicated issues they are grappling with and may feel they need a few months or more to understand and resolve their issues. Other people come with long-standing problems or difficult feelings and may benefit from longer-term therapy.</p>
    <h3>How long are the sessions?</h3>
    <p class="answer-gap">Typically, each session is 50 minutes provided in person at my practice in Westbury, or online using a platform such as MeetRoom or CallNest.</p>
    <h3>How much is each session?</h3>
    <p>I charge £50 per session.</p>
  </div>
</section>

<!-- Blog -->
<section class="page" style="height:956px">
  <header class="site-header">
    <div class="brand"><span class="brand-mark"></span><span class="brand-name">Rosalind Faber</span></div>
    <div class="contact-bar">
      <span><svg width="12" height="9" viewBox="0 0 12 9"><rect x="0.5" y="0.5" width="11" height="8" fill="none" stroke="#2e2e2e"/><path d="M0.5 0.5 6 5 11.5 0.5" fill="none" stroke="#2e2e2e"/></svg>rosalindfaber@gentlerooms.co.uk</span>
      <span><svg width="10" height="10" viewBox="0 0 10 10"><path d="M2 0.5 4 3 3 4.3a6 6 0 0 0 2.7 2.7L7 6l2.5 2-1.2 1.5C4.5 9.5 0.5 5.5 0.5 1.7Z" fill="#2e2e2e"/></svg>07700 900418</span>
    </div>
  </header>
  <aside class="sidebar">
    <ul class="nav"><li>homepage</li><li>about me</li><li>therapy</li><li>common questions</li><li class="active">blog</li><li>contact me</li></ul>
    <div class="social"><span></span><span></span><span></span></div>
  </aside>
  <article class="main blog">
    <h3>Trauma and the bears – a fable</h3>
    <p>Once upon a time … there were humans on the savannah. It's a dangerous world. We need to find food, we need to protect ourselves from predators, we need shelter, we need to find a mate. And we do this by clanning together in tribes of 70-100 people. No tribe, no reproduction. No tribe, no sharing of resources. No tribe, no safety from the bears. We survive everything, including trauma, by being in a tribe.</p>
    <p>So we're humans on the savannah. We're not bigger or faster than other predators, and we don't have fangs or claws. Our safety is in numbers and in being alert to threat. That hypervigilance might stop us sleeping at night, it might make us jittery and anxious, but better a nervous human than a dead one. We communicate complexly with other humans, live collaboratively: this is how we survive. Our tribe is everything. We cannot survive alone, and so we must avoid isolation at all costs. Shame is the means through which we learn to avoid behaviours which would have us ejected from our tribe. Shame is a survival mechanism.</p>
    <p>So we're humans on the savannah. Every day, the same dilemma: we need to go out to hunt and to gather. But going out – out there, amongst predators with fangs and claws, is dangerous. A bear swipe might mean death now, or later via infection. But if we stay in the camp we'll starve. In the savannah heat, food spoils quickly, so what we kill today, we eat today. And tomorrow we go out again. Berries or bears: approach or avoid? Every day we have to face this dilemma. Do we avoid danger or do we seek resources?</p>
    <p>So we're humans on the savannah and today we're down by the river looking for berries. But there's a sound in the bushes. We go still. We strain eyes and ears to locate the threat. And before we know it, we're off in flight. Run. Get away. There's a bear in the bushes, so we need to flee from it before it even sees us. React now, think later: better safe than sorry. Being preemptively fearful gives us a survival advantage: we avoid the places where bears lurk. Anxiety is a survival mechanism. Then if unwittingly we stumble into bear territory, we avoid – instantly, over-reactively – with flight.</p>
    <h3 class="later">Why the symptoms of trauma make sense</h3>
    <p>I looked again at the list of symptoms. It was long, and overwhelming, and ran to more than two pages. 'Signs you've been traumatised' promised the infographic. Many of them were cross-referenced – meticulously, helpfully, well-meaningly – to the diagnostic criteria for PTSD in the psychiatric 'bibles' of mental disorders, the DSM-5 and the ICD-11. This was an impressive, and somewhat intimidating list. More worrying was that I identified with so many of the items on it.</p>
    <p>So this was me, then: a tick-box list of symptoms demonstrating how screwed up I was. 'Loser!' it screamed at me, casually. The more items I ticked, the more it screamed: 'Bigger loser!' Forty items – tick, tick, tick: 'Biggest loser in the world!' And so shame sat like a heavy puddle of tar in my stomach. I didn't want to admit to anyone that I had flashbacks, that I was constantly hyperaroused and hyper-vigilant, that I had problems sleeping, that I felt perpetually depressed or agitated, that I had 'labile affect' (whatever that was), that I had low self-esteem, that I had amnesia, that I had difficulties in relationships, that I had struggled to maintain a 'sense of self'. In short, I didn't want to admit that I was quite as much a loser as this list implied.</p>
  </article>
</section>

<!-- Contact me -->
<section class="page" style="height:749px">
  <header class="site-header">
    <div class="brand"><span class="brand-mark"></span><span class="brand-name">Rosalind Faber</span></div>
    <div class="contact-bar">
      <span><svg width="12" height="9" viewBox="0 0 12 9"><rect x="0.5" y="0.5" width="11" height="8" fill="none" stroke="#2e2e2e"/><path d="M0.5 0.5 6 5 11.5 0.5" fill="none" stroke="#2e2e2e"/></svg>rosalindfaber@gentlerooms.co.uk</span>
      <span><svg width="10" height="10" viewBox="0 0 10 10"><path d="M2 0.5 4 3 3 4.3a6 6 0 0 0 2.7 2.7L7 6l2.5 2-1.2 1.5C4.5 9.5 0.5 5.5 0.5 1.7Z" fill="#2e2e2e"/></svg>07700 900418</span>
    </div>
  </header>
  <aside class="sidebar">
    <ul class="nav"><li>homepage</li><li>about me</li><li>therapy</li><li>common questions</li><li>blog</li><li class="active">contact me</li></ul>
    <div class="social"><span></span><span></span><span></span></div>
  </aside>
  <form class="contact-form">
    <div class="field">Name, Surname</div>
    <div class="field">E-mail</div>
    <div class="field message">Your message</div>
    <div class="send">send message</div>
  </form>
  <address class="contact-info">
    <div>Address:</div>
    <div>Elmbank Community Centre</div>
    <div>27 Hollybrook Road</div>
    <div>Westbury Green</div>
    <div>WB3 7QL</div>
    <div class="gap">Contact info:</div>
    <div>www.rosalindfaber.co.uk</div>
    <div>rosalindfaber@gentlerooms.co.uk</div>
    <div>07700 900418</div>
  </address>
</section>

</body>
</html>
```